New Business Card Design Project - RK Ledgerwise & Filing Partners, LLC

Below is a sample image of the card (TM Bookkeeping). I would like to have a designed business card that looks very similar (Front & Back). In addition, I would like to keep the same colors as well. I attached my Business Logo (RK Ledgerwise & Filing Partners, LLC) that will be on my website.

Target Market(s)

Executives, Business Owners, Board of Directors, Chief Financial Officers

Contact Information for Business Card

Font styles to use
Serif

Colors
0c5ba6
ffffff
5c5c5c

Requirements
Must have
• My Name: Malcolm Ferris, CPA
• Position: Owner
• Phone: (240) 555-0148
• Email: Mferris@rkledgerwise.example
• Website: www.Rkledgerwise.example
• Address: 4736 Ferncliff Ave #2093
• Dunmore Falls, MD 21990
Nice to have
• Same design & color scheme as TM Bookkeepnig Business card sample attached

```html
<!DOCTYPE html>
<html lang="en">
<head>
<meta charset="utf-8">
<title>RK Ledgerwise &amp; Filing Partners – Business Card</title>
<link href="https://fonts.googleapis.com/css2?family=Tinos&family=Noto+Sans:wght@400&display=swap" rel="stylesheet">
<style>
  :root {
    --brand-blue: #0c5ba6;
    --brand-grey: #5c5c5c;
    --card-white: #f5f5f5;
    --ink: #111111;
    --backdrop: #c6c6c8;
    --serif: "Tinos", "Times New Roman", serif;
    --sans: "Noto Sans", Arial, sans-serif;
  }
  * { margin: 0; padding: 0; box-sizing: border-box; }
  html, body { width: 1200px; height: 1200px; overflow: hidden; }
  body { background: var(--backdrop); position: relative; }

  .card {
    position: absolute;
    left: 250px;
    width: 698px;
    height: 400px;
    overflow: hidden;
  }
  .card--front { top: 150px; background: var(--card-white); }
  .card--back  { top: 630px; background: var(--brand-blue); }

  .brand {
    position: absolute;
    display: flex;
    align-items: center;
    gap: 16px;
    font-family: var(--serif);
    font-weight: 400;
    letter-spacing: 1px;
    white-space: nowrap;
  }
  .brand__mark { display: block; flex: none; }
  .card--front .brand { left: 54px; top: 68px; font-size: 28px; color: var(--brand-blue); }
  .card--front .brand__mark { width: 40px; height: 40px; background: var(--brand-blue); }
  .card--back .brand { left: 92px; top: 176px; font-size: 25px; color: #ffffff; }
  .card--back .brand__mark { width: 36px; height: 36px; background: #ffffff; }

  .holder { position: absolute; left: 52px; top: 200px; font-family: var(--sans); color: var(--ink); }
  .holder__name { font-size: 24px; line-height: 30px; }
  .holder__role { font-size: 18px; line-height: 24px; }

  .contact {
    position: absolute;
    left: 386px;
    top: 208px;
    list-style: none;
    font-family: var(--sans);
    font-size: 17px;
    line-height: 19px;
    color: var(--ink);
  }
  .contact__item { display: flex; align-items: flex-start; gap: 8px; margin-bottom: 5px; }
  .contact__item--address { margin-top: 8px; }
  .contact__icon { width: 18px; height: 18px; flex: none; fill: var(--brand-blue); }

  .footer-bands { position: absolute; left: 0; bottom: 0; width: 698px; height: 33px; display: block; }
</style>
</head>
<body>

<section class="card card--front" aria-label="Card front">
  <div class="brand">
    <span class="brand__mark"></span>
    <span class="brand__name">RK LEDGERWISE &amp; FILING PARTNERS</span>
  </div>

  <div class="holder">
    <p class="holder__name">Malcolm Ferris, CPA</p>
    <p class="holder__role">Owner</p>
  </div>

  <ul class="contact">
    <li class="contact__item">
      <svg class="contact__icon" viewBox="0 0 24 24"><path d="M6.6 10.8a15 15 0 0 0 6.6 6.6l2.2-2.2a1 1 0 0 1 1-.25 11.4 11.4 0 0 0 3.6.57 1 1 0 0 1 1 1V20a1 1 0 0 1-1 1A17 17 0 0 1 3 4a1 1 0 0 1 1-1h3.5a1 1 0 0 1 1 1c0 1.25.2 2.45.57 3.57a1 1 0 0 1-.25 1z"/></svg>
      <span>(240) 555-0148</span>
    </li>
    <li class="contact__item">
      <svg class="contact__icon" viewBox="0 0 24 24"><path d="M2 5h20v14H2zm2 2v.5l8 5 8-5V7zm0 2.9V17h16V9.9l-8 5z"/></svg>
      <span>Mferris@rkledgerwise.example</span>
    </li>
    <li class="contact__item">
      <svg class="contact__icon" viewBox="0 0 24 24"><path d="M12 2a10 10 0 1 0 0 20 10 10 0 0 0 0-20zm6.9 6h-3a15 15 0 0 0-1.4-3.9A8 8 0 0 1 18.9 8zM12 4a13 13 0 0 1 1.9 4h-3.8A13 13 0 0 1 12 4zM4.3 14a8 8 0 0 1 0-4h3.4a16 16 0 0 0 0 4zm.8 2h3a15 15 0 0 0 1.4 3.9A8 8 0 0 1 5.1 16zm3-8h-3a8 8 0 0 1 4.4-3.9A15 15 0 0 0 8.1 8zM12 20a13 13 0 0 1-1.9-4h3.8A13 13 0 0 1 12 20zm2.3-6H9.7a14 14 0 0 1 0-4h4.6a14 14 0 0 1 0 4zm.2 5.9a15 15 0 0 0 1.4-3.9h3a8 8 0 0 1-4.4 3.9zm1.8-5.9a16 16 0 0 0 0-4h3.4a8 8 0 0 1 0 4z"/></svg>
      <span>www.Rkledgerwise.example</span>
    </li>
    <li class="contact__item contact__item--address">
      <svg class="contact__icon" viewBox="0 0 24 24"><path d="M12 2a7 7 0 0 0-7 7c0 5 7 13 7 13s7-8 7-13a7 7 0 0 0-7-7zm0 9.5A2.5 2.5 0 1 1 12 6.5a2.5 2.5 0 0 1 0 5z"/></svg>
      <span>4736 Ferncliff Ave #2093<br>Dunmore Falls, MD 21990</span>
    </li>
  </ul>

  <svg class="footer-bands" viewBox="0 0 698 33" preserveAspectRatio="none" aria-hidden="true">
    <rect x="0" y="0" width="698" height="33" fill="var(--brand-blue)"/>
    <polygon points="0,8 318,8 335,33 0,33" fill="#ffffff"/>
    <polygon points="0,12 312,12 326,33 0,33" fill="var(--brand-grey)"/>
  </svg>
</section>

<section class="card card--back" aria-label="Card back">
  <div class="brand">
    <span class="brand__mark"></span>
    <span class="brand__name">RK LEDGERWISE &amp; FILING PARTNERS</span>
  </div>
</section>

</body>
</html>
```